Box design for velomacrate

VelomaCrate ackage design development brief.
Technical specification:
Package measurements – 200x200x40mm or 150x150x60mm (see pictures of an example below).
Design only for outer layer, no printing inside.
As the box itself is the main product, the aim of this design is to be outstanding – modern, clean,
sophisticated, attractive, memorable and providing WoW-effect to the consumer.

Industry/Entity Type

Printing

```html
<!DOCTYPE html>
<html lang="en">
<head>
<meta charset="utf-8">
<title>VelomaCrate – Box Lid Design</title>
<link rel="stylesheet" href="https://fonts.googleapis.com/css2?family=Raleway:wght@300&display=swap">
<style>
  :root {
    --page-bg: #ffffff;
    --lid-border: #3a3a44;
    --tone-rose: #f1e2e5;
    --tone-blush: #f8eeef;
    --tone-sky: #e9f0f8;
    --tone-mist: #f7f9f8;
    --tone-lilac: #ece9f0;
    --brand-text: #8a8a8e;
    --brand-mark: #a85568;
  }
  html, body {
    margin: 0;
    padding: 0;
    width: 1200px;
    height: 1000px;
    overflow: hidden;
    background: var(--page-bg);
  }
  .canvas {
    position: relative;
    width: 1200px;
    height: 1000px;
  }
  .lid {
    position: absolute;
    left: 200px;
    top: 100px;
    width: 800px;
    height: 800px;
    box-sizing: border-box;
    border: 1px solid var(--lid-border);
    overflow: hidden;
  }
  .lid-pattern {
    position: absolute;
    inset: 0;
    background:
      linear-gradient(135deg,
        var(--tone-lilac) 0%,
        var(--tone-blush) 18%,
        var(--tone-rose) 32%,
        var(--tone-mist) 46%,
        var(--tone-sky) 60%,
        var(--tone-blush) 74%,
        var(--tone-mist) 100%);
  }
  .brand {
    position: absolute;
    right: 24px;
    bottom: 22px;
    display: flex;
    flex-direction: column;
    align-items: center;
    gap: 18px;
  }
  .brand-square {
    width: 44px;
    height: 44px;
    background: var(--brand-mark);
  }
  .brand-name {
    font-family: "Raleway", sans-serif;
    font-weight: 300;
    font-size: 33px;
    letter-spacing: 1px;
    color: var(--brand-text);
    line-height: 1;
  }
</style>
</head>
<body>
  <main class="canvas">
    <section class="lid">
      <div class="lid-pattern" role="img" aria-label="Soft diagonal gingham check pattern in pale rose, sky blue and white"></div>
      <div class="brand">
        <div class="brand-square"></div>
        <div class="brand-name">VELOMACRATE</div>
      </div>
    </section>
  </main>
</body>
</html>
```